Book Title: “Ember: Road of Quiet Dawn” Please see the attachment “Text on the cover”.

Book Cover Design Instructions: This book is meant for people of all religions and nationalities. Therefore, on the cover, there should be no mosque or an object specific to any religion. The primary emphasis should be on the "unconditional love of God." Therefore, use universal symbols of love. The second priority themes could be Sufism, Peace, and self-improvement. Rest is your imagination. Please also see the attachment: 'Book description and author's Bio.'
This book has the potential to be a best seller. Please do a good job.
What Book Cover Formats are required: A designer should submit cover designs in three formats: (1) eBook, (2) Paperback, and (3) Hardback. These books will be published on Velmora PBX.
Format requirements for eBooks are available from: https://pbx.velmora-press.example/en_US/help/topic/R731928405.
You can find paperback and hardback cover measurements from: https://pbx.velmora-press.example/en_US/cover-calculator
• To complete the project, all three formats should be accepted by Velmora PBX.
• The book interior trim size is 6.14 X 9.21 inches.
• Interior Type: Premium color.
• No bleed.
• I do not upload barcode. So, the back cover should have room for Velmora to print the barcode.
• Number of pages 126.
Compensation for the designer: After selecting one designer, I will increase the amount by $200 on Artlumo to compensate for three deliverables.
Follow-up of the Project:
After the book is published, I may need minor revisions. For example, the number of pages may change. Therefore, I will need the same design in revised sizes. In that case, I will pay $25 for each revision. For example, if the number of pages changes, I will need a different spine for paperback and hardback, then I will pay the artist $25 + $25 = $50 for both designs.
List of Enclosers:
1. Text on the cover.
2. Book description and author's Bio for the back cover.
3. Later, I will upload my picture for the book's back cover.

Target Market(s)

Any adult

Industry/Entity Type

Any industry

Requirements
Must have
• Three Deliverables

```html
<!DOCTYPE html>
<html lang="en">
<head>
<meta charset="utf-8">
<title>Ember: Road of Quiet Dawn — Book Cover</title>
<link href="https://fonts.googleapis.com/css2?family=Bebas+Neue&family=Montserrat:wght@700;800&display=swap" rel="stylesheet">
<style>
  :root {
    --page-bg: #ececec;
    --cover-navy: #0b0b8c;
    --cover-navy-deep: #06065e;
    --title-white: #ffffff;
    --accent-yellow: #ffd800;
    --band-yellow: #ffcc00;
    --author-ink: #111111;
  }
  html, body {
    margin: 0;
    padding: 0;
    width: 1200px;
    height: 1200px;
    overflow: hidden;
    background: var(--page-bg);
  }
  .canvas {
    display: block;
    width: 1200px;
    height: 1200px;
  }
  .title-display {
    font-family: "Bebas Neue", "Oswald", sans-serif;
    fill: var(--title-white);
  }
  .title-accent { fill: var(--accent-yellow); }
  .subtitle {
    font-family: "Montserrat", sans-serif;
    font-weight: 800;
    font-size: 64px;
    fill: var(--title-white);
  }
  .author-name {
    font-family: "Montserrat", sans-serif;
    font-weight: 700;
    font-size: 71px;
    fill: var(--author-ink);
  }
  .rule { stroke: var(--title-white); stroke-width: 3; }
</style>
</head>
<body>
<svg class="canvas" viewBox="0 0 1932 1932" xmlns="http://www.w3.org/2000/svg">
  <defs>
    <linearGradient id="coverGradient" x1="0" y1="0" x2="1" y2="1">
      <stop offset="0" stop-color="var(--cover-navy-deep)"/>
      <stop offset="0.35" stop-color="var(--cover-navy)"/>
      <stop offset="1" stop-color="var(--cover-navy)"/>
    </linearGradient>
  </defs>

  <g class="book-cover">
    <rect class="cover-background" x="374" y="33" width="1251" height="1875" fill="url(#coverGradient)"
          role="img" aria-label="Deep navy background with a faint tonal geometric pattern"/>

    <text class="title-display title-main" x="458" y="540" font-size="607"
          textLength="1085" lengthAdjust="spacingAndGlyphs">EMBER</text>

    <line class="rule" x1="458" y1="638" x2="730" y2="638"/>
    <text class="title-display title-connector" x="755" y="713" font-size="200"
          textLength="493" lengthAdjust="spacing">ROAD OF</text>
    <line class="rule" x1="1268" y1="638" x2="1543" y2="638"/>

    <text class="title-display title-accent" x="1000" y="1032" font-size="417"
          text-anchor="middle" letter-spacing="10">QUIET</text>

    <text class="title-display title-main" x="458" y="1590" font-size="746"
          textLength="1085" lengthAdjust="spacingAndGlyphs">DAWN</text>

    <text class="subtitle" x="458" y="1665" textLength="1082" lengthAdjust="spacingAndGlyphs">GUIDE TO CULTIVATING INNER</text>
    <text class="subtitle" x="485" y="1745" textLength="1030" lengthAdjust="spacingAndGlyphs">PEACE AND MINDFUL LIVING</text>

    <rect class="author-band" x="374" y="1785" width="1251" height="123" fill="var(--band-yellow)"/>
    <text class="author-name" x="578" y="1870" textLength="842" lengthAdjust="spacing">DR. NAVEEN IDRIS</text>
  </g>
</svg>
</body>
</html>
```